WebApp for IoT (Glim lights and Tarvo/Mellobin)

I am going to create my own dashbord for Quillon Pro (See other examples on https://quillondeck.io/) But I want it much more flexible and advanced.
One page per room (So I can have an Tabrix in each room with all functions just for that room) and include controls for light (both overall for the room and in an popupwindow all lightbulbs n the room - se more about how its done in Varnell Glim app on https://www.varnell-glim.com/en-us/explore-glim/apps/bridge) aswell as set volume/track for Tarvo.

I want the final solution to be "skinable" so I can choose from Blue-CSS to Green-CSS etc, but at this moment I only want ONE color!

I have added an PDF with the functions I am thinking of, but the design is for you to create!

Please have in mind it will be running on Tabrixes on the wall, and in the mobile.

For the moment I only want an PSD of the "Room page", "Light popup" and "Sound Popup", but I might contract the winner to get HTML/CSS as second step.

```html
<!DOCTYPE html>
<html lang="en">
<head>
<meta charset="utf-8">
<title>Room Control WebApp</title>
<link href="https://fonts.googleapis.com/css2?family=Poppins:wght@400;500;600;700;800&display=swap" rel="stylesheet">
<style>
:root{
  --page-bg:#ada5a3;
  --screen-top:#dedede;
  --screen-bottom:#cbcbcd;
  --card:#c6c6c9;
  --card-soft:rgba(190,190,194,.75);
  --pill-border:#c2c2c5;
  --ink:#1e1f23;
  --ink-soft:#3a3b40;
  --line:#bdbdc0;
  --toggle:#b3b3b7;
  --knob:#f4f4f5;
  --star:#d4922a;
  --sun:#f2b418;
  --cloud:#bfd9ea;
}
*{box-sizing:border-box;margin:0;padding:0}
html,body{width:1200px;height:2246px;overflow:hidden}
body{background:var(--page-bg);font-family:"Poppins",sans-serif;color:var(--ink);position:relative}
.screen{position:absolute;left:215px;width:770px;height:481px;border-radius:3px;
  background:linear-gradient(135deg,var(--screen-top),var(--screen-bottom));overflow:hidden}
.screen--room{top:279px}
.screen--light{top:909px}
.screen--sound{top:1545px}
.abs{position:absolute}
.head-icon{width:54px;height:54px;border-radius:50%;background:var(--card);display:flex;align-items:center;justify-content:center}
.title{font-weight:800;font-size:33px;letter-spacing:-.3px;line-height:1}
.divider{height:1px;background:var(--line)}
.card{background:var(--card-soft);border-radius:8px;display:flex;align-items:center}
.toggle{width:44px;height:22px;border-radius:11px;background:var(--toggle);position:relative;margin-left:auto}
.toggle::after{content:"";position:absolute;right:3px;top:3px;width:16px;height:16px;border-radius:50%;background:var(--knob)}
.pill{height:44px;border:1.5px solid var(--pill-border);border-radius:22px;display:flex;align-items:center;padding-left:5px;gap:10px;font-weight:500;font-size:15px}
.play{width:34px;height:34px;border-radius:50%;background:var(--ink);display:flex;align-items:center;justify-content:center;flex:none}
.play svg{width:12px;height:12px}
.tile{width:133px;height:141px;border-radius:8px;background:var(--card-soft);display:flex;flex-direction:column;align-items:center;padding-top:22px}
.tile svg{width:60px;height:66px}
.tile-label{margin-top:12px;font-weight:500;font-size:15px}
.playlist-item{position:absolute;left:21px;right:20px;height:40px;display:flex;align-items:center;justify-content:space-between;font-size:16px;color:var(--ink-soft);border-bottom:1px solid var(--line)}
.playlist-item:last-child{border-bottom:none}
</style>
</head>
<body>

<!-- Room page -->
<section class="screen screen--room" aria-label="Room page">
  <div class="head-icon abs" style="left:31px;top:46px">
    <svg width="28" height="22" viewBox="0 0 28 22" fill="none" stroke="#1e1f23" stroke-width="1.8"><rect x="3" y="2" width="22" height="9" rx="2"/><rect x="1" y="11" width="26" height="6" rx="1"/><path d="M3 17v3M25 17v3M7 11V7h5v4M16 11V7h5v4"/></svg>
  </div>
  <h1 class="title abs" style="left:96px;top:57px">ROOM</h1>

  <svg class="abs" style="left:320px;top:44px" width="66" height="56" viewBox="0 0 66 56" aria-hidden="true">
    <g stroke="#f2b418" stroke-width="2" stroke-linecap="round"><path d="M38 2v6M54 9l-4 4M60 24h-6M22 9l4 4M16 24h6"/></g>
    <circle cx="38" cy="25" r="12" fill="#f2b418"/>
    <path d="M8 52a8 8 0 0 1 0-16a12 12 0 0 1 22-6a10 10 0 0 1 18 8a7 7 0 0 1 0 14z" fill="#bfd9ea"/>
  </svg>
  <div class="abs" style="left:394px;top:42px;font-size:33px;font-weight:500;line-height:1">23°<span style="font-weight:400">C</span></div>
  <div class="abs" style="left:395px;top:78px;font-size:17px;font-weight:500">Sunny</div>

  <svg class="abs" style="left:618px;top:55px" width="32" height="32" viewBox="0 0 32 32" fill="none" stroke="#1e1f23" stroke-width="1.8"><circle cx="16" cy="16" r="14"/><path d="M16 7v9l6 5"/></svg>
  <div class="abs" style="left:662px;top:52px;font-size:13px;font-weight:600;line-height:1.4">2022-07-14<br>15:23</div>

  <div class="divider abs" style="left:30px;width:710px;top:132px"></div>

  <svg class="abs" style="left:79px;top:186px" width="20" height="20" viewBox="0 0 24 24"><path d="M12 1l3.2 7 7.6.8-5.7 5.1 1.6 7.6L12 17.6 5.3 21.5l1.6-7.6L1.2 8.8 8.8 8z" fill="#d4922a"/></svg>
  <div class="card abs" style="left:113px;top:189px;width:303px;height:81px;padding:0 20px 0 18px">
    <svg width="34" height="38" viewBox="0 0 34 38" fill="none" stroke="#1e1f23" stroke-width="1.8"><path d="M17 2v6M7 20a10 10 0 0 1 20 0zM4 20h26M12 20a5 5 0 0 0 10 0M17 28v6M9 26l-3 4M25 26l3 4"/></svg>
    <span style="font-size:20px;font-weight:500;margin-left:12px">Light Details</span>
    <div class="toggle"></div>
  </div>

  <svg class="abs" style="left:79px;top:284px" width="20" height="20" viewBox="0 0 24 24"><path d="M12 1l3.2 7 7.6.8-5.7 5.1 1.6 7.6L12 17.6 5.3 21.5l1.6-7.6L1.2 8.8 8.8 8z" fill="#d4922a"/></svg>
  <div class="card abs" style="left:113px;top:286px;width:303px;height:81px;padding:0 20px 0 18px">
    <svg width="34" height="30" viewBox="0 0 34 30" fill="none" stroke="#1e1f23" stroke-width="1.8"><path d="M2 10h6l8-7v24l-8-7H2zM21 10a6 6 0 0 1 0 10M25 6a11 11 0 0 1 0 18M29 3a15 15 0 0 1 0 24"/></svg>
    <span style="font-size:20px;font-weight:500;margin-left:12px">Sound Details</span>
    <div class="toggle"></div>
  </div>

  <div class="abs" style="left:500px;top:189px;width:1px;height:227px;background:var(--line)"></div>

  <div class="pill abs" style="left:570px;top:190px;width:120px"><span class="play"><svg viewBox="0 0 12 12"><path d="M3 1l8 5-8 5z" fill="#fff"/></svg></span>Flow 1</div>
  <div class="pill abs" style="left:570px;top:250px;width:120px"><span class="play"><svg viewBox="0 0 12 12"><path d="M3 1l8 5-8 5z" fill="#fff"/></svg></span>Flow 2</div>
  <div class="pill abs" style="left:570px;top:310px;width:120px"><span class="play"><svg viewBox="0 0 12 12"><path d="M3 1l8 5-8 5z" fill="#fff"/></svg></span>Flow 3</div>
  <div class="pill abs" style="left:570px;top:371px;width:120px"><span class="play"><svg viewBox="0 0 12 12"><path d="M3 1l8 5-8 5z" fill="#fff"/></svg></span>Flow 4</div>
</section>

<!-- Light popup -->
<section class="screen screen--light" aria-label="Light details">
  <div class="head-icon abs" style="left:29px;top:44px">
    <svg width="28" height="32" viewBox="0 0 34 38" fill="none" stroke="#1e1f23" stroke-width="2"><path d="M17 2v6M7 20a10 10 0 0 1 20 0zM4 20h26M12 20a5 5 0 0 0 10 0M17 28v6M9 26l-3 4M25 26l3 4"/></svg>
  </div>
  <h1 class="title abs" style="left:98px;top:56px">LIGHT DETAILS</h1>

  <div class="tile abs" style="left:30px;top:129px">
    <svg viewBox="0 0 60 66" fill="none" stroke="#1e1f23" stroke-width="1.8"><path d="M30 2v20M18 36a12 12 0 0 1 24 0zM10 36h40M24 36a6 6 0 0 0 12 0M30 48v8M20 46l-4 7M40 46l4 7M12 42l-5 3M48 42l5 3"/></svg>
    <span class="tile-label">Tropical</span>
  </div>
  <div class="tile abs" style="left:175px;top:129px">
    <svg viewBox="0 0 60 66" fill="none" stroke="#1e1f23" stroke-width="1.8"><path d="M6 4h48M10 8h40M16 8v26M30 8v38M44 8v26"/><circle cx="16" cy="38" r="5"/><circle cx="30" cy="51" r="6"/><circle cx="44" cy="38" r="5"/></svg>
    <span class="tile-label">Sunrise</span>
  </div>
  <div class="tile abs" style="left:320px;top:129px">
    <svg viewBox="0 0 60 66" fill="none" stroke="#1e1f23" stroke-width="1.8"><path d="M24 6h12l-2 8h-8zM4 38a26 24 0 0 1 52 0zM4 38h52M20 38a10 8 0 0 0 20 0M30 50v7M20 48l-3 6M40 48l3 6"/></svg>
    <span class="tile-label">Concentrate</span>
  </div>
  <div class="tile abs" style="left:464px;top:129px">
    <svg viewBox="0 0 60 66" fill="none" stroke="#1e1f23" stroke-width="1.8"><path d="M30 2v14M16 36a14 14 0 0 1 28 0zM12 36h36M24 36a6 6 0 0 0 12 0M30 48v7M21 46l-4 6M39 46l4 6"/></svg>
    <span class="tile-label">Dimmed</span>
  </div>
  <div class="tile abs" style="left:608px;top:129px">
    <svg viewBox="0 0 60 66" fill="none" stroke="#1e1f23" stroke-width="1.8"><path d="M30 18v34M22 52h16M20 60h20M24 52v8M36 52v8M30 22L8 14l-4 10 18 8zM30 22l22-8 4 10-18 8zM22 18l8 4 8-4"/></svg>
    <span class="tile-label">Night</span>
  </div>

  <div class="divider abs" style="left:31px;width:714px;top:312px"></div>

  <div class="pill abs" style="left:31px;top:354px;width:118px"><span class="play"><svg viewBox="0 0 12 12"><path d="M3 1l8 5-8 5z" fill="#fff"/></svg></span>Bulb 1</div>
  <div class="pill abs" style="left:163px;top:354px;width:118px"><span class="play"><svg viewBox="0 0 12 12"><path d="M3 1l8 5-8 5z" fill="#fff"/></svg></span>Bulb 2</div>
  <div class="pill abs" style="left:295px;top:354px;width:118px"><span class="play"><svg viewBox="0 0 12 12"><path d="M3 1l8 5-8 5z" fill="#fff"/></svg></span>Bulb 3</div>
  <div class="pill abs" style="left:426px;top:354px;width:118px"><span class="play"><svg viewBox="0 0 12 12"><path d="M3 1l8 5-8 5z" fill="#fff"/></svg></span>Bulb 4</div>
</section>

<!-- Sound popup -->
<section class="screen screen--sound" aria-label="Sound details">
  <div class="head-icon abs" style="left:27px;top:43px">
    <svg width="28" height="24" viewBox="0 0 34 30" fill="none" stroke="#1e1f23" stroke-width="2"><path d="M2 10h6l8-7v24l-8-7H2zM21 10a6 6 0 0 1 0 10M25 6a11 11 0 0 1 0 18M29 3a15 15 0 0 1 0 24"/></svg>
  </div>
  <h1 class="title abs" style="left:98px;top:55px">SOUND DETAILS</h1>

  <div class="card abs" style="left:28px;top:130px;width:231px;height:81px;padding:0 16px 0 18px">
    <span class="play"><svg viewBox="0 0 12 12"><path d="M3 1l8 5-8 5z" fill="#fff"/></svg></span>
    <span style="font-size:20px;font-weight:500;margin-left:10px">Play</span>
    <div class="toggle"></div>
  </div>
  <div class="card abs" style="left:274px;top:130px;width:231px;height:81px;padding:0 16px 0 20px">
    <span class="play"><svg viewBox="0 0 12 12"><path d="M3 1l8 5-8 5z" fill="#fff"/></svg></span>
    <span style="font-size:20px;font-weight:500;margin-left:10px">Volume</span>
    <div class="toggle"></div>
  </div>

  <div class="abs" style="left:521px;top:130px;width:221px;height:302px;border-radius:8px;background:var(--card-soft)">
    <div class="abs" style="left:18px;top:22px;display:flex;align-items:center;gap:10px">
      <span class="play"><svg viewBox="0 0 12 12"><path d="M1 3h10l-5 8z" fill="#fff"/></svg></span>
      <span style="font-size:19px;font-weight:500">Playlist</span>
    </div>
    <div class="playlist-item" style="top:76px">Room<span>›</span></div>
    <div class="playlist-item" style="top:116px">Light<span>›</span></div>
    <div class="playlist-item" style="top:156px">Flow<span>›</span></div>
    <div class="playlist-item" style="top:196px">Sound<span>›</span></div>
    <div class="playlist-item" style="top:236px;border-bottom:none">PlayList<span>›</span></div>
  </div>
</section>

</body>
</html>
```